General brochure with course listing

A general brochure for the Global Jurist Academy, about 40 A5 pages that includes mission, vision, history, descriptions of our technical assistance and capacity building programming and detailed descriptions of our courses. Would be for both online pdf (magazine style) and print. I have attached an example of an older one that was satisfactory but not as professional as what we're looking for now.

Target Market(s)

Lawyers and government officials around the world.

Industry/Entity Type

Legal and capacity building

Requirements
Must have
• A good design and template that we can replicate on our own in InDesign annually. We need the layout from you and we will provide the copy. We will also publish as a pdf
Nice to have
• Colors and branding from our website - www.gja-example.org

```html
<!DOCTYPE html>
<html lang="en">
<head>
<meta charset="utf-8">
<title>Global Jurist Academy – Brochure Spread 20–21</title>
<link rel="stylesheet" href="https://fonts.googleapis.com/css2?family=Poppins:wght@300;400&display=swap">
<style>
  :root {
    --page-white: #ffffff;
    --brand-blue: #25408f;
    --accent-orange: #e2582a;
    --text-dark: #231f20;
    --text-light: #ffffff;
  }
  * { margin: 0; padding: 0; box-sizing: border-box; }
  html, body { width: 1200px; height: 423px; overflow: hidden; background: var(--page-white); }
  body { font-family: "Poppins", sans-serif; color: var(--text-dark); }

  .spread { position: relative; width: 1200px; height: 423px; display: flex; }

  /* Left page */
  .page-left { position: relative; width: 600px; height: 423px; background: var(--page-white); }
  .section-title {
    position: absolute; left: 36px; top: 34px;
    font-weight: 300; font-size: 13.2px; letter-spacing: 0.1px;
    color: var(--accent-orange);
  }
  .column {
    position: absolute; top: 66px; width: 168px;
    font-size: 8.7px; line-height: 13.4px; font-weight: 400;
    letter-spacing: -0.2px;
    text-align: justify; hyphens: auto;
  }
  .column p + p { margin-top: 13.4px; }
  .column-one { left: 36px; }
  .column-two { left: 216px; }
  .drop-cap {
    float: left; font-size: 46px; line-height: 36px; font-weight: 400;
    margin: 3px 2px 0 -1px; letter-spacing: 0;
  }
  .feature-photo {
    position: absolute; left: 396px; top: 68px; width: 168px; height: 206px;
    background: linear-gradient(110deg, #e9c9a6 0%, #d98a3a 30%, #a86a2f 48%, #6d6a55 70%, #3f4a36 100%);
  }
  .callout {
    position: absolute; left: 396px; top: 309px; width: 168px;
    display: flex; gap: 6px; align-items: stretch;
  }
  .callout-bar { flex: none; width: 9px; background: var(--accent-orange); }
  .callout-text {
    font-size: 8.6px; line-height: 13.4px; letter-spacing: -0.15px;
    color: var(--accent-orange);
  }
  .folio-left {
    position: absolute; left: 45px; top: 396px; font-size: 9.6px;
  }
  .rule-left {
    position: absolute; left: 60px; top: 402px; width: 503px; height: 1px;
    background: var(--accent-orange);
  }

  /* Right page */
  .page-right { position: relative; width: 600px; height: 423px; background: var(--brand-blue); color: var(--text-light); }
  .world-map {
    position: absolute; left: 64px; top: 33px; width: 473px; height: 237px;
    background: radial-gradient(ellipse at 55% 40%, rgba(255,255,255,0.24), rgba(255,255,255,0.1) 70%);
    border-radius: 4px;
  }
  .map-markers { position: absolute; left: 0; top: 0; width: 600px; height: 423px; }
  .map-label { position: absolute; font-size: 9.6px; color: var(--text-light); }
  .page-title {
    position: absolute; left: 34px; top: 292px;
    font-weight: 400; font-size: 46px; line-height: 1; letter-spacing: -0.3px;
  }
  .rule-right {
    position: absolute; left: 36px; top: 400px; width: 503px; height: 1px;
    background: var(--accent-orange);
  }
  .folio-right { position: absolute; left: 546px; top: 394px; font-size: 9.6px; }
</style>
</head>
<body>
<div class="spread">
  <section class="page-left">
    <h2 class="section-title">INTERNATIONAL INVESTMENT LAW CENTER</h2>

    <div class="column column-one">
      <p><span class="drop-cap">P</span>ellia net voles providia veru­ment. Voluptatem rat vid et delest aut iunt odis nimus ali­quas susdaes molent a dolor reicid molore veliscitios dissint, tem facest venderum quaspelest maio offic te vi­duntiur sin por ab ius dipsa quibus ut la quiaecatur?</p>
      <p>Lorerna tatibus antiis utemqui cone­cus, corem net volorru ptaquis alita­tius que por aut as dollorio et mo te volorerunt alis as debit, aut dendis do­loreh enduntia cus et ma velluptiis re nam autemquate int anihic tota volor­ib usaped quo volupta enducipitat qui untistrum quidendene nos ullaut ali­bus ea comnimetur autempo restrum serferi vellabo.</p>
      <p>Henis que mo volor sequi quatem autam delessim quatia verro conse­quia nonsect emquidus, qui tem. Atur,</p>
    </div>

    <div class="column column-two">
      <p>cum que ommollit quoditisque dem dolupta is enis alitatur, sit dipsam volluptatis ma ipissi omnient inverit iuntios sinvend esteseq uunture et aut venimetust, sectemp orepern atiosa quaepuditat.</p>
      <p>Puditi blandaeptas experum fugia quos ipsam intibus voloriores min eat­ectessum, sint omnihic tibus, conse­quid ut explatur am at ut optibus net aspelenem volupta tumquis eos aut dolorem ped</p>
      <p>Poreptat emolupt aepelic iminciis pel­ignitatur re volut ped quo es eatium ullacer sperorero voluptatiis enihic to consequo torrovi dentem ipis arum et voloruptas sin es doluptatio qui inis es ullaccabo. Equi conseque eum est iunt estist, none sant, solorehent quaspera volo volluptatur?</p>
    </div>

    <div class="feature-photo" role="img" aria-label="Photograph of a globe beside stacked shipping containers, representing international trade and investment"></div>

    <aside class="callout">
      <span class="callout-bar"></span>
      <p class="callout-text">For more information on the sem­inars, please consult pages 26-30 or contact us at training@gja-example.org.</p>
    </aside>

    <span class="folio-left">20</span>
    <span class="rule-left"></span>
  </section>

  <section class="page-right">
    <div class="world-map" role="img" aria-label="Stylised white world map with flags marking regional centers in Egypt, Nigeria, Uganda and Chile"></div>

    <svg class="map-markers" viewBox="0 0 600 423" aria-hidden="true">
      <g stroke="#1b2a5e" stroke-width="0.8" fill="none">
        <polyline points="322,150 332,159 341,159"/>
        <polyline points="283,176 273,186 272,200"/>
        <polyline points="334,181 344,189 351,189"/>
        <polyline points="191,260 198,267 206,267"/>
      </g>
      <g fill="#1b2a5e">
        <circle cx="322" cy="150" r="1.8"/>
        <circle cx="283" cy="176" r="1.8"/>
        <circle cx="334" cy="181" r="1.8"/>
        <circle cx="191" cy="260" r="1.8"/>
      </g>
    </svg>

    <span class="map-label" style="left:341px; top:150px;">Egypt</span>
    <span class="map-label" style="left:253px; top:204px;">Nigeria</span>
    <span class="map-label" style="left:355px; top:182px;">Uganda</span>
    <span class="map-label" style="left:210px; top:261px;">Chile</span>

    <h1 class="page-title">Regional Centers</h1>
    <span class="rule-right"></span>
    <span class="folio-right">21</span>
  </section>
</div>
</body>
</html>
```